Orrin Fernhouse Plant Hire WEB

Orrin Fernhouse are a small family owned business specialising in hire of indoor horticultural plants. They have been operating for more than 20 years in the local New Zealand market providing long and short term plant hire for businesses and events.

They offer a wide range of mostly tropical and indigenous plants for hire and Orrin Fernhouse staff maintain all hire plants on a regular basis.

MORE PHOTOS AVAILABLE ON REQUEST if required

Please note - this should be a small 3 pager - home/about - products - gallery
Contact Us can be a button or on home page. Note - this is a small owner operated business.

Target Market(s)

Commercial, offices, entrance foyers, receptions, restaurants, promotions, trade shows, events, corporate and private functions

Industry/Entity Type

Business

Requirements
Must have
• Must remain integral to existing branding and include the current company logo. Should maintain existing corporate colours. Requires an enquiry page for people to contact the company via email (this can be a mailto page), also requires a page explaining about the company, and one detailing the types of hire available together with types of plans for hire. The site also needs a gallery that can be added to over time to show the various plants and their applications.
Nice to have
• It would be nice to have a facility on the gallery where a couple of detail lines could be added to explain the plant types, location etc

PREFER A WORDPRESS SOLUTION - BUT OPEN TO SUGGESTIONS
Should not have
• The site should not be overly complex. It should be simple for the client to self manage (add/ remove photos, edit text) It should be quick to load and simple to navigate.

```html
<!DOCTYPE html>
<html lang="en">
<head>
<meta charset="utf-8">
<title>Orrin Fernhouse Plant Hire</title>
<link rel="stylesheet" href="https://fonts.googleapis.com/css2?family=Source+Sans+3:wght@400;600;700&display=swap">
<style>
:root{
  --ink:#111;
  --navy:#2b3f86;
  --blue:#1f6fd6;
  --orange:#f07c1a;
  --orange-dark:#c85c08;
  --band:#e9e9e9;
  --band-line:#b9b9b9;
  --line-soft:#f3c9a6;
  --leaf-dark:#3d5a2e;
  --leaf:#8fae6a;
  --glass:#d9e6e9;
}
*{box-sizing:border-box;margin:0;padding:0}
html,body{width:1200px;height:2439px;overflow:hidden;background:#fff}
body{position:relative;font-family:"Source Sans 3",Arial,sans-serif;color:var(--ink)}
.abs{position:absolute}

/* header */
.site-header{left:0;top:0;width:1200px;height:60px;background:#fff;border-bottom:5px solid var(--orange)}
.brand{left:312px;top:10px;display:flex;align-items:center;gap:8px;font-size:24px;font-weight:700;color:var(--navy)}
.brand-dot{width:14px;height:14px;border-radius:50%;background:var(--navy)}
.contact-strip{top:12px;font-size:13px;display:flex;align-items:center;gap:6px}
.contact-strip svg{width:14px;height:14px}
.main-nav{left:505px;top:40px;display:flex;gap:0;font-size:12px}
.main-nav a{color:var(--ink);text-decoration:none;padding:2px 12px}
.main-nav a.is-current{background:var(--blue);color:#fff;border-radius:3px}

/* hero */
.hero{left:0;top:65px;width:1200px;height:435px;background:linear-gradient(180deg,#bcc9c4 0%,#d8e2dc 40%,#9fb089 70%,#c9ccc4 100%);border-bottom:4px solid var(--orange)}
.hero-arrow{top:210px;width:93px;height:95px;background:var(--orange);display:flex;align-items:center;justify-content:center}
.hero-arrow svg{width:44px;height:60px}
.hero-panel{left:683px;top:107px;width:385px;height:313px;background:rgba(255,255,255,.55);border-radius:8px;padding:36px 30px}
.hero-panel h1{font-size:30px;font-weight:700;margin-bottom:22px}
.hero-panel p{font-size:14.5px;line-height:1.35}
.btn{display:flex;align-items:center;justify-content:center;background:var(--orange);color:#fff;font-weight:700;border:2px solid var(--orange-dark);border-radius:4px}
.hero-panel .btn{position:absolute;left:171px;top:261px;width:119px;height:32px;font-size:15px}

/* about */
.section-title{font-size:30px;font-weight:400;white-space:nowrap}
.section-title b{font-weight:700}
.rule{height:2px;background:#b8c8e8}
.about-text{left:310px;top:566px;width:375px;font-size:14px;line-height:1.3}
.about-text p+p{margin-top:18px}
.why-list{left:722px;top:562px;list-style:none;font-size:13px}
.why-list li{display:flex;align-items:center;gap:10px;height:32px}
.why-list svg{width:16px;height:16px}

/* products */
.band{left:0;width:1200px;background:var(--band);border-top:3px solid var(--band-line);border-bottom:3px solid var(--band-line)}
.slider-btn{top:762px;width:20px;height:20px;display:flex;align-items:center;justify-content:center}
.product-card{top:800px;width:134px}
.product-card .photo{height:93px;background:linear-gradient(160deg,#dfe6e4,#8aa46c 60%,#6b6a5e)}
.product-card h3{font-size:15px;font-weight:700;margin-top:5px;line-height:1}
.product-card p{font-size:6.5px;line-height:1.25;margin-top:2px}

/* offer */
.offer-item{display:flex;gap:8px}
.offer-item .dot{width:15px;height:15px;border-radius:50%;background:var(--blue);margin-top:3px;flex:none}
.offer-item h4{font-size:18px;font-weight:400;line-height:1.1}
.offer-item p{font-size:10px;margin-top:2px}

/* gallery */
.gallery-frame{width:142px;height:103px;border:7px solid var(--blue);background:linear-gradient(160deg,#e3eaea,#9bb27c 55%,#5e6757)}

/* contact */
.map{left:307px;top:1800px;width:586px;height:210px;background:linear-gradient(135deg,#e8e6df,#d5dccf 50%,#e6e1d4);border:1px solid #bbb}
.field{border:2px solid var(--line-soft);background:#fff}
.submit{left:778px;top:2349px;width:117px;height:34px;font-size:19px}
.site-footer{left:0;top:2420px;width:1200px;height:19px;background:#000}
</style>
</head>
<body>

<header class="site-header abs">
  <div class="brand abs"><span class="brand-dot"></span>Orrin Fernhouse</div>
  <div class="contact-strip abs" style="left:620px">
    <svg viewBox="0 0 16 16"><rect width="16" height="16" rx="3" fill="#1f6fd6"/><path d="M5 3l2 2-1 2 3 3 2-1 2 2-2 2C7 13 3 9 3 5z" fill="#fff"/></svg>
    +036-555-0142
  </div>
  <div class="contact-strip abs" style="left:760px">
    <svg viewBox="0 0 16 16"><rect width="16" height="16" rx="3" fill="#1f6fd6"/><path d="M3 5h10v7H3z M3 5l5 4 5-4" fill="none" stroke="#fff" stroke-width="1.4"/></svg>
    hello@orrinfernhouse.example
  </div>
  <nav class="main-nav abs">
    <a class="is-current" href="#">Home</a>
    <a href="#">About us</a>
    <a href="#">Our Products</a>
    <a href="#">Gallery</a>
    <a href="#">Contact Us</a>
  </nav>
</header>

<section class="hero abs" role="img" aria-label="Office window with a long planter of snake plants on white pebbles">
  <div class="hero-arrow abs" style="left:0">
    <svg viewBox="0 0 44 60"><path d="M32 6L10 30l22 24" fill="none" stroke="#fff" stroke-width="9"/></svg>
  </div>
  <div class="hero-arrow abs" style="left:1107px">
    <svg viewBox="0 0 44 60"><path d="M12 6l22 24-22 24" fill="none" stroke="#fff" stroke-width="9"/></svg>
  </div>
  <div class="hero-panel abs">
    <h1>Lorem Ipsum</h1>
    <p>Orrin Fernhouse is a small family owned business specialising in hire of indoor horticultural plants. They have been operating for more than 20 years in the local New Zealand market providing long and short term plant hire for businesses and events.</p>
    <a class="btn" href="#">Read More</a>
  </div>
</section>

<h2 class="section-title abs" style="left:310px;top:522px"><b>Who</b> we are</h2>
<div class="rule abs" style="left:458px;top:541px;width:237px"></div>
<div class="about-text abs">
  <p>We can enhance your workplace by introducing quality indoor plants in attractive planters. Creating a natural green environment with Orrin Fernhouse plants will help improve indoor air quality, increase staff wellness and productivity.</p>
  <p>Our range of tropical and native plants will enhance your conference or event by creating a more relaxing atmosphere for your delegates or clients. Orrin Fernhouse staff can advise on plant arrangement, deliver and setup for each event.</p>
</div>

<h2 class="section-title abs" style="left:710px;top:522px"><b>Why us?</b></h2>
<div class="rule abs" style="left:822px;top:541px;width:70px"></div>
<ul class="why-list abs">
  <li><svg viewBox="0 0 16 16"><rect width="16" height="16" rx="2" fill="#1f6fd6"/><path d="M3.5 8.5l3 3 6-7" fill="none" stroke="#fff" stroke-width="2"/></svg>On-site advice and quotes</li>
  <li><svg viewBox="0 0 16 16"><rect width="16" height="16" rx="2" fill="#1f6fd6"/><path d="M3.5 8.5l3 3 6-7" fill="none" stroke="#fff" stroke-width="2"/></svg>7 day per week service</li>
  <li><svg viewBox="0 0 16 16"><rect width="16" height="16" rx="2" fill="#1f6fd6"/><path d="M3.5 8.5l3 3 6-7" fill="none" stroke="#fff" stroke-width="2"/></svg>Competitive hire charges</li>
  <li><svg viewBox="0 0 16 16"><rect width="16" height="16" rx="2" fill="#1f6fd6"/><path d="M3.5 8.5l3 3 6-7" fill="none" stroke="#fff" stroke-width="2"/></svg>Efficient and friendly</li>
  <li><svg viewBox="0 0 16 16"><rect width="16" height="16" rx="2" fill="#1f6fd6"/><path d="M3.5 8.5l3 3 6-7" fill="none" stroke="#fff" stroke-width="2"/></svg>Regular plant maintenance</li>
  <li><svg viewBox="0 0 16 16"><rect width="16" height="16" rx="2" fill="#1f6fd6"/><path d="M3.5 8.5l3 3 6-7" fill="none" stroke="#fff" stroke-width="2"/></svg>Quality plants and planters</li>
</ul>

<section class="band abs" style="top:751px;height:205px"></section>
<h2 class="section-title abs" style="left:310px;top:746px"><b>Our</b> products</h2>
<div class="slider-btn abs" style="left:845px;background:#8a8a8a"><svg width="10" height="12" viewBox="0 0 10 12"><path d="M8 1L2 6l6 5" fill="none" stroke="#fff" stroke-width="2"/></svg></div>
<div class="slider-btn abs" style="left:868px;background:var(--navy)"><svg width="10" height="12" viewBox="0 0 10 12"><path d="M2 1l6 5-6 5" fill="none" stroke="#fff" stroke-width="2"/></svg></div>

<article class="product-card abs" style="left:310px">
  <div class="photo" role="img" aria-label="Snake plants in a pebble planter by an office window"></div>
  <h3>Lorem ipsum</h3>
  <p>Lorem ipsum dolor sit amet, consectetur adipiscing elit, sed do eiusmod tempor incididunt ut labore.</p>
</article>
<article class="product-card abs" style="left:461px">
  <div class="photo" role="img" aria-label="Row of square planters with snake plants"></div>
  <h3>Lorem ipsum</h3>
  <p>Lorem ipsum dolor sit amet, consectetur adipiscing elit, sed do eiusmod tempor incididunt ut labore.</p>
</article>
<article class="product-card abs" style="left:610px">
  <div class="photo" role="img" aria-label="Leafy green plants in a long planter"></div>
  <h3>Lorem ipsum</h3>
  <p>Lorem ipsum dolor sit amet, consectetur adipiscing elit, sed do eiusmod tempor incididunt ut labore.</p>
</article>
<article class="product-card abs" style="left:756px">
  <div class="photo" role="img" aria-label="Snake plants in a planter by a window"></div>
  <h3>Lorem ipsum</h3>
  <p>Lorem ipsum dolor sit amet, consectetur adipiscing elit, sed do eiusmod tempor incididunt ut labore.</p>
</article>

<h2 class="section-title abs" style="left:310px;top:987px"><b>What</b> we offer</h2>
<div class="offer-item abs" style="left:386px;top:1050px"><span class="dot"></span><div><h4>Enhances the appearance</h4><p>Lorem ipsum dolor sit amet, consectetur adip.</p></div></div>
<div class="offer-item abs" style="left:386px;top:1107px"><span class="dot"></span><div><h4>Natural and tranquil</h4><p>Lorem ipsum dolor sit amet, consectetur adip.</p></div></div>
<div class="offer-item abs" style="left:386px;top:1165px"><span class="dot"></span><div><h4>Variety and Versatility</h4><p>Lorem ipsum dolor sit amet, consectetur adip.</p></div></div>
<div class="offer-item abs" style="left:635px;top:1050px"><span class="dot"></span><div><h4>No staff down time</h4><p>Lorem ipsum dolor sit amet, consectetur adip.</p></div></div>
<div class="offer-item abs" style="left:635px;top:1107px"><span class="dot"></span><div><h4>Calming atmosphere</h4><p>Lorem ipsum dolor sit amet, consectetur adip.</p></div></div>
<div class="offer-item abs" style="left:635px;top:1165px"><span class="dot"></span><div><h4>Speciment plants</h4><p>Lorem ipsum dolor sit amet, consectetur adip.</p></div></div>

<section class="band abs" style="top:1249px;height:488px"></section>
<h2 class="section-title abs" style="left:310px;top:1258px"><b>Gallery</b></h2>
<div class="gallery-frame abs" style="left:358px;top:1327px" role="img" aria-label="Snake plants in an office planter"></div>
<div class="gallery-frame abs" style="left:539px;top:1327px" role="img" aria-label="Snake plants in an office planter"></div>
<div class="gallery-frame abs" style="left:717px;top:1327px" role="img" aria-label="Snake plants in an office planter"></div>
<div class="gallery-frame abs" style="left:358px;top:1463px" role="img" aria-label="Snake plants in an office planter"></div>
<div class="gallery-frame abs" style="left:539px;top:1463px" role="img" aria-label="Snake plants in an office planter"></div>
<div class="gallery-frame abs" style="left:717px;top:1463px" role="img" aria-label="Snake plants in an office planter"></div>
<div class="gallery-frame abs" style="left:358px;top:1600px" role="img" aria-label="Snake plants in an office planter"></div>
<div class="gallery-frame abs" style="left:539px;top:1600px" role="img" aria-label="Snake plants in an office planter"></div>
<div class="gallery-frame abs" style="left:717px;top:1600px" role="img" aria-label="Snake plants in an office planter"></div>

<h2 class="section-title abs" style="left:310px;top:1750px;font-size:28px"><b>Contact us</b></h2>
<div class="map abs" role="img" aria-label="Street map showing the business location"></div>
<div class="field abs" style="left:305px;top:2051px;width:288px;height:39px"></div>
<div class="field abs" style="left:605px;top:2051px;width:288px;height:39px"></div>
<div class="field abs" style="left:305px;top:2110px;width:588px;height:217px"></div>
<a class="btn submit abs" href="#">submit</a>

<footer class="site-footer abs"></footer>
</body>
</html>
```